Business card design needed

We are a Landscape business based in Sydney. We are targeting upper class clients that have the money to spend on their gardens.
We design, construct and maintain the gardens that we create.
We are looking for modern business card with our logo on it and the colours green grey\black/white scale. The design should communicate modern creative gardens. it should look classy and have a professional feel to it not cheap.should be two sides to the business card. Back side to have the words design construct maintain with possible the vine attached somewhere.
Updates

Project Deadline Extended
Reason: Hi Guys. Some of you have asked for a vector version of the vine so I just need some more time to find it as I don't have it here on my computer. Keep up the good work! Thanks Jonah

Hi guys and girls.
You have all done a really good job so far. I have recently uploaded the vector for the vine and the logo as promissed. Looking forward to seeing you use them in your designs. Also i would like to see the words design-construct-maintain on the card as an option maybe on the back.
Thanks .

Target Market(s)

white collar, higher education, high social group in affluent areas

Industry/Entity Type

Business

Contact Information for Business Card

Willowmere Terrace Landscapes
Jonah Pellworth- 0431 592 074 Director( only need one name and number per card i.e. same design twice with different number and name.)
Felix arnsby- 0417 265 309 Director
www.wtlandscapes.com.au
ABN-286 731 904
Lic- 518064C

Requirements
Must have
• Logo which I am trying to upload but it is not working. I have contacted pixel bazaar to try and fix this.
Should not have
• Two s

```html
<!DOCTYPE html>
<html lang="en">
<head>
<meta charset="utf-8">
<title>Willowmere Terrace Landscapes — Business Card</title>
<link rel="stylesheet" href="https://fonts.googleapis.com/css2?family=Dancing+Script:wght@700&family=Ubuntu:wght@400;500;700&display=swap">
<style>
  :root {
    --backdrop: #d9d9d9;
    --card-black: #050505;
    --card-white: #ffffff;
    --leaf-green: #8cc63f;
    --leaf-green-soft: #c9e6a2;
    --vine-white: #e8e8e8;
    --ink: #111111;
    --logo-grey: #d6d6d6;
  }
  * { box-sizing: border-box; margin: 0; padding: 0; }
  html, body {
    width: 1200px;
    height: 814px;
    overflow: hidden;
    background: var(--backdrop);
  }
  .canvas {
    position: relative;
    width: 1200px;
    height: 814px;
    display: flex;
    justify-content: center;
    align-items: center;
    gap: 90px;
  }
  .card {
    position: relative;
    width: 400px;
    height: 660px;
    overflow: hidden;
    box-shadow: 0 10px 28px rgba(0,0,0,0.28);
  }

  /* Front side */
  .card--front { background: var(--card-black); }
  .brand {
    position: absolute;
    top: 56px;
    left: 0;
    width: 100%;
    text-align: center;
    font-family: "Ubuntu", sans-serif;
    font-weight: 500;
    font-size: 24px;
    line-height: 1.2;
    letter-spacing: 0.5px;
    color: var(--logo-grey);
  }
  .tagline {
    position: absolute;
    top: 132px;
    left: 0;
    width: 100%;
    text-align: center;
    font-family: "Dancing Script", cursive;
    font-weight: 700;
    font-size: 21px;
    color: var(--leaf-green);
  }
  .vine-art {
    position: absolute;
    left: 0;
    bottom: 0;
    width: 100%;
    height: 430px;
    background:
      radial-gradient(ellipse at 60% 75%, rgba(140,198,63,0.55), rgba(140,198,63,0) 65%),
      radial-gradient(ellipse at 35% 60%, rgba(232,232,232,0.25), rgba(232,232,232,0) 60%),
      linear-gradient(180deg, var(--card-black) 0%, #1a2410 100%);
  }

  /* Back side */
  .card--back {
    background: var(--card-white);
    text-align: center;
  }
  .corner-sprig {
    position: absolute;
    background: radial-gradient(ellipse at center, var(--leaf-green-soft), rgba(201,230,162,0) 70%);
  }
  .corner-sprig--top-left { top: 0; left: 0; width: 90px; height: 60px; }
  .corner-sprig--top-right { top: 0; right: 0; width: 120px; height: 90px; }
  .corner-sprig--bottom { bottom: 0; left: 110px; width: 170px; height: 100px; }
  .corner-sprig--bottom-right { bottom: 40px; right: 0; width: 70px; height: 80px; }
  .corner-sprig--left { bottom: 150px; left: 0; width: 80px; height: 70px; }

  .holder {
    position: absolute;
    top: 86px;
    left: 0;
    width: 100%;
  }
  .holder__name {
    font-family: "Dancing Script", cursive;
    font-weight: 700;
    font-size: 38px;
    color: var(--leaf-green);
    line-height: 1.1;
  }
  .holder__role {
    font-family: "Ubuntu", sans-serif;
    font-weight: 700;
    font-size: 21px;
    letter-spacing: 1px;
    color: var(--ink);
    margin-top: 4px;
  }
  .details {
    position: absolute;
    top: 232px;
    left: 0;
    width: 100%;
    list-style: none;
  }
  .details__item { margin-bottom: 18px; }
  .details__label {
    display: block;
    font-family: "Ubuntu", sans-serif;
    font-weight: 500;
    font-size: 21px;
    color: var(--leaf-green);
    letter-spacing: 0.5px;
  }
  .details__value {
    display: block;
    font-family: "Ubuntu", sans-serif;
    font-weight: 700;
    font-size: 19px;
    color: var(--ink);
    letter-spacing: 1px;
  }
  .website {
    position: absolute;
    top: 470px;
    left: 0;
    width: 100%;
    font-family: "Dancing Script", cursive;
    font-weight: 700;
    font-size: 25px;
    color: var(--leaf-green);
  }
</style>
</head>
<body>
<main class="canvas">
  <section class="card card--front" aria-label="Business card front">
    <p class="brand">Willowmere Terrace<br>Landscapes</p>
    <p class="tagline">Design-Construct-Maintain</p>
    <div class="vine-art" role="img" aria-label="Flowing vine illustration with green and white curling stems and leaves"></div>
  </section>

  <section class="card card--back" aria-label="Business card back">
    <div class="corner-sprig corner-sprig--top-left" role="img" aria-label="Small green vine sprig"></div>
    <div class="corner-sprig corner-sprig--top-right" role="img" aria-label="Green vine sprig with leaves"></div>
    <div class="corner-sprig corner-sprig--left" role="img" aria-label="Small green leaf"></div>
    <div class="corner-sprig corner-sprig--bottom" role="img" aria-label="Green vine stems with leaves"></div>
    <div class="corner-sprig corner-sprig--bottom-right" role="img" aria-label="Green curling vine tendril"></div>

    <header class="holder">
      <h1 class="holder__name">Jonah Pellworth</h1>
      <p class="holder__role">DIRECTOR</p>
    </header>

    <ul class="details">
      <li class="details__item">
        <span class="details__label">ABN</span>
        <span class="details__value">286 731 904</span>
      </li>
      <li class="details__item">
        <span class="details__label">LICENCE NO:</span>
        <span class="details__value">518064 C</span>
      </li>
      <li class="details__item">
        <span class="details__label">PHONE NO:</span>
        <span class="details__value">0431 592 074</span>
      </li>
    </ul>

    <p class="website">www.wtlandscapes.com.au</p>
  </section>
</main>
</body>
</html>
```